Graphic to hang inside of fitness studio

This graphic will be printed on vinyl and hung inside of a boutique fitness studio for 2019. Graphic should read YEAR OF POSSIBILITIES.

2018 was called Year of Living Well. We would like something on trend for 2019 to hang within the studio as our 2019 Mantra. It is not a logo but for internal use. I've attached our logo here and the website is www.kestrelmovehall.com for additional reference. Thank you.

Target Market(s)

25 to 45 women

Industry/Entity Type

Fitness

Colors

Designer to choose colors to be used in the design.

Requirements
Must have
• On trend for 2019. (no people in image)
• Year of Possibilities in trendy font.
• Easy to read.
• Need text only.
• Do not need graphic images.
Nice to have
• Tintorell colours for 2019
• 2019 design trends for background
Should not have
• Male dominate colour or masculine traits.
• Photos of fitness.
• Photos of people.
• Photos of equipment.

```html
<!DOCTYPE html>
<html lang="en">
<head>
<meta charset="utf-8">
<title>Year of Possibilities – Kestrel Move Hall</title>
<link href="https://fonts.googleapis.com/css2?family=Antonio:wght@100;700&family=Roboto+Condensed:wght@300&display=swap" rel="stylesheet">
<style>
  :root {
    --stage: #03070a;
    --coral: #e8826d;
    --coral-deep: #d96f5c;
    --coral-light: #ef9d87;
    --blush: #f6e4dc;
    --accent: #e05e48;
    --white: #ffffff;
  }
  html, body {
    margin: 0;
    width: 1200px;
    height: 1200px;
    overflow: hidden;
    background: var(--stage);
  }
  .banner {
    position: absolute;
    left: 336px;
    top: 67px;
    width: 528px;
    height: 1066px;
  }
  .banner svg { display: block; }
  .studio-name {
    font-family: "Antonio", sans-serif;
    font-weight: 700;
    font-size: 23px;
    fill: var(--accent);
  }
  .mantra-lead {
    font-family: "Roboto Condensed", sans-serif;
    font-weight: 300;
    font-size: 60px;
    fill: var(--blush);
  }
  .mantra-word {
    font-family: "Antonio", sans-serif;
    font-weight: 100;
    font-size: 170px;
    fill: var(--white);
    stroke: var(--accent);
    stroke-width: 5;
    stroke-linejoin: round;
    paint-order: stroke;
  }
</style>
</head>
<body>
  <main class="banner">
    <svg width="528" height="1066" viewBox="0 0 528 1066" xmlns="http://www.w3.org/2000/svg">
      <defs>
        <radialGradient id="wash" cx="0.55" cy="0.33" r="0.75">
          <stop offset="0" stop-color="var(--coral-light)"/>
          <stop offset="0.6" stop-color="var(--coral)"/>
          <stop offset="1" stop-color="var(--coral-deep)"/>
        </radialGradient>
      </defs>
      <rect class="backdrop" width="528" height="1066" fill="var(--blush)"/>
      <path class="watercolour-wash" role="img" aria-label="Soft coral watercolour wash with a ragged lower edge"
        fill="url(#wash)"
        d="M0 0 H528 V815 L505 830 L480 850 L470 875 L455 870 L430 905 L410 925 L392 940 L380 960 L360 975 L345 950 L330 965 L315 940 L300 960 L282 945 L265 935 L245 955 L225 950 L210 935 L190 945 L170 925 L150 915 L130 930 L110 920 L90 935 L70 945 L55 910 L40 905 L22 885 L0 875 Z"/>
      <text class="studio-name" x="167" y="160" textLength="187" lengthAdjust="spacingAndGlyphs">KESTREL MOVE HALL</text>
      <text class="mantra-lead" x="43" y="446" textLength="192" lengthAdjust="spacingAndGlyphs">YEAR OF</text>
      <text class="mantra-word" x="45" y="599" textLength="432" lengthAdjust="spacingAndGlyphs">Possibilities</text>
    </svg>
  </main>
</body>
</html>
```